E-learning Information & Community Website Needs a Makeover

I'm looking for a design makeover for my website "Vetrola.club". Vetrola's aim is to connect people to online learning through forums, information, guides & independent reviews. The site was launched in September 2014 using a forum software (Xenforo), but now needs a more polished and sophisticated look which communicates expertise and professionalism. I would like to see designs that use the current "Vetrola" blue (#0070c0). To visit the current website, go to http://www.vetrola.club/

Target Market(s)

People wishing to study online

Industry/Entity Type

Club

Number of Pages Required

4 page

Font styles to use
Sans Serif

Requirements
Must have
• A simple, clear and sophisticated lading page with links to the site's key features: discussion forums, Useful resources, Reviews, News etc, Articles. (See layout idea file attached)
• The main pages are the Landing Page, Discussion Forums, Resources & Reviews
• I would like to see designs that use the current "Vetrola" blue (#0070c0).
Nice to have
• Something uncluttered and easy to understand. The design should convey expertise in the field of online learning, giving users a sense of trust in the site's offerings.
• To give an idea of the sort of thing I'm after, take a look at brantivo.com website (screenshot attached)

```html
<!DOCTYPE html>
<html lang="en">
<head>
<meta charset="utf-8">
<title>Vetrola – Connecting People to Online Learning</title>
<link rel="stylesheet" href="https://fonts.googleapis.com/css2?family=Open+Sans:wght@300;400;600&display=swap">
<style>
:root{
  --brand:#0070c0;
  --link:#2a9fd6;
  --ink:#333;
  --muted:#8a8a8a;
  --bar:#141414;
  --panel:#f2f2f2;
  --rule:#d8d8d8;
  --head:#d4d4d4;
  --nav:#bdbdbd;
}
*{box-sizing:border-box;margin:0;padding:0}
html,body{width:960px;height:1200px;overflow:hidden}
body{font-family:"Open Sans",Arial,sans-serif;color:var(--ink);background:#fff;position:relative}
a{text-decoration:none;color:inherit}

.topbar{height:33px;background:var(--bar);position:relative}
.brand{position:absolute;left:180px;top:-3px;color:#a9d3f2;font-size:20px;line-height:22px}
.brand small{display:block;font-size:8.5px;color:#fff;line-height:10px;margin-top:1px}
.mainnav{position:absolute;left:374px;top:10px;display:flex;gap:12px;font-size:9px;color:var(--nav)}
.mainnav .current{color:#fff}
.mainnav .login{color:var(--link);margin-left:6px}

.hero{position:relative;height:200px;background:linear-gradient(180deg,#4f9ad8 0%,#a9cdee 45%,#d9e8f3 68%,#7cae3c 82%,#4f7f22 100%)}
.hero-photo{position:absolute;inset:0}
.hero h1{position:absolute;left:192px;top:25px;font-weight:400;font-size:25px;line-height:30px;color:#222}
.signup{position:absolute;left:192px;top:127px;background:var(--brand);color:#fff;font-size:9.5px;padding:4px 12px;border-radius:11px;border:1px solid #0a4f87}

.features{background:var(--panel);height:259px;padding-top:20px}
.feature-grid{width:615px;margin-left:173px;display:grid;grid-template-columns:repeat(3,1fr);grid-template-rows:110px 115px}
.feature{display:flex;flex-direction:column;align-items:center;justify-content:center;font-size:15px;color:#444;position:relative}
.feature svg{width:38px;height:38px;margin-bottom:12px}
.feature:nth-child(3n+1),.feature:nth-child(3n+2){border-right:1px solid var(--rule)}
.feature:nth-child(-n+3)::after{content:"";position:absolute;bottom:0;left:50px;right:50px;border-bottom:1px solid var(--rule)}

.section-title{text-align:center;font-weight:400;font-size:24px;line-height:32px;color:#111}
.topics .section-title{margin-top:16px}
.partner-strip{width:607px;margin:4px auto 0;height:58px;background:#f8f8f8;display:flex;align-items:center;gap:22px;padding:0 6px;font-size:12px;color:#9a9a9a}
.partner-strip .arrow{font-size:10px;color:#111}
.partner-dot{width:34px;height:34px;border-radius:50%;background:#cfcfcf}
.partner-box{width:22px;height:34px;background:#d6d6d6}

.community .section-title{margin-top:38px}
.thread-head{margin-top:12px;height:24px;background:var(--head);font-size:10.5px;color:#222;position:relative}
.thread-head span{position:absolute;top:5px}
.threads{width:600px;margin-left:180px}
.thread{display:flex;align-items:center;border-bottom:1px solid #e2e2e2;height:44px}
.thread:first-child{height:46px}
.thread.tall{height:48px}
.avatar{width:30px;height:30px;flex:none;margin-right:10px;background:var(--brand);color:#fff;font-size:7.5px;line-height:9px;text-align:center;padding-top:6px;border-radius:2px}
.avatar.photo{background:linear-gradient(#8a6a55,#5a4030);border-radius:3px}
.avatar.blank{background:#f3f3f3;border:1px solid #ddd}
.thread-main{width:320px;font-size:12.5px;color:var(--link);line-height:15px}
.tag{display:inline-block;font-size:9.5px;color:#222;padding:0 4px;line-height:13px;border-radius:2px;margin-right:3px}
.tag.article{background:#e81d1d;color:#fff}
.tag.courses{background:#f5a300}
.tag.news{background:#bdbdbd}
.tag.event{background:#8d8d8d}
.tag.advice{background:#86d98a}
.meta{display:block;font-size:8.5px;color:var(--muted);line-height:11px}
.stats{width:110px;border-left:1px solid var(--rule);border-right:1px solid var(--rule);padding:0 8px;font-size:12px;color:var(--muted);display:grid;grid-template-columns:1fr auto;line-height:14px}
.stats .num{color:#333}
.stats .sm{font-size:8.5px}
.last{flex:1;text-align:right;font-size:12px;color:var(--link);line-height:13px}
.last .meta{font-size:8.5px}
.pager{position:absolute;left:765px;top:1092px;font-size:10px;line-height:12px;color:#111}

.footer{position:absolute;left:0;bottom:0;width:960px;height:84px;background:var(--bar)}
.social{position:absolute;left:265px;top:18px;display:flex;gap:3px}
.social i{width:14px;height:14px;border-radius:50%}
.newsletter{position:absolute;left:358px;top:12px;width:240px;height:21px;background:#fff;font-size:8.5px;font-style:italic;color:#222;padding:4px 8px}
.subscribe{position:absolute;left:606px;top:17px;font-size:8.5px;font-style:italic;color:var(--link)}
.footnav{position:absolute;left:269px;top:53px;display:flex;gap:11px;font-size:8.5px;color:var(--nav)}
.footnav .current{color:#fff}
.footnav .login{color:var(--link)}
</style>
</head>
<body>
<header class="topbar">
  <a class="brand" href="#">Vetrola<small>Connecting People to Online Learning</small></a>
  <nav class="mainnav">
    <a class="current" href="#">Home</a><a href="#">Forums</a><a href="#">Resources</a><a href="#">Members</a><a href="#">FAQ</a><a href="#">Blog</a><a href="#">Vetrola Español</a><a href="#">Course Scoop</a><a class="login" href="#">Login</a>
  </nav>
</header>

<section class="hero">
  <div class="hero-photo" role="img" aria-label="Photo of a man sitting in a grassy meadow with a laptop, arms raised toward a blue sky"></div>
  <h1>At the heart of connecting people<br>to online learning</h1>
  <a class="signup" href="#">Signup for free</a>
</section>

<section class="features">
  <div class="feature-grid">
    <a class="feature" href="#"><svg viewBox="0 0 40 40"><g fill="#444"><circle cx="20" cy="20" r="12"/><g stroke="#444" stroke-width="6"><path d="M20 3v34M3 20h34M8 8l24 24M32 8L8 32"/></g></g><circle cx="20" cy="20" r="5" fill="#f2f2f2"/></svg>Getting Started</a>
    <a class="feature" href="#"><svg viewBox="0 0 40 40"><circle cx="20" cy="20" r="17" fill="#444"/><g fill="#f2f2f2"><circle cx="12" cy="20" r="2.6"/><circle cx="20" cy="20" r="2.6"/><circle cx="28" cy="20" r="2.6"/></g></svg>Discussions</a>
    <a class="feature" href="#"><svg viewBox="0 0 40 40"><path d="M3 20Q20 4 37 20Q20 36 3 20Z" fill="none" stroke="#444" stroke-width="3"/><circle cx="20" cy="20" r="6" fill="#444"/></svg>Reviews</a>
    <a class="feature" href="#"><svg viewBox="0 0 40 40"><path d="M12 36V14a2 2 0 014 0v-8a2 2 0 014 0v6a2 2 0 014 0v2a2 2 0 014 0v14c0 5-3 8-8 8z" fill="#444"/></svg>Tips &amp; Guidelines</a>
    <a class="feature" href="#"><svg viewBox="0 0 40 40"><path d="M34 20A14 14 0 1120 6" fill="none" stroke="#444" stroke-width="3"/><path d="M20 1l6 5-6 5z" fill="#444"/><text x="20" y="24" font-size="11" font-weight="600" text-anchor="middle" fill="#444" font-family="Open Sans,sans-serif">24</text></svg>News &amp; Articles</a>
    <a class="feature" href="#"><svg viewBox="0 0 40 40"><path d="M6 3h14v26H6z" fill="#444"/><path d="M14 10h12l6 6v22H14z" fill="#444" stroke="#f2f2f2" stroke-width="2"/></svg>Newsletter</a>
  </div>
</section>

<section class="topics">
  <h2 class="section-title">Frequent Topics</h2>
  <div class="partner-strip">
    <span class="arrow">◀</span><span class="partner-dot"></span>
    <span>Harlow Vale</span><span>Brenmoor</span><span>TALVEN</span><span>Ostrand College</span><span>Redfield Global</span>
    <span class="partner-box"></span><span class="arrow">▶</span>
  </div>
</section>

<section class="community">
  <h2 class="section-title">From the Community</h2>
  <div class="thread-head"><span style="left:193px">Recent Threads</span><span style="left:492px">Start Date</span><span style="left:555px">Replies</span><span style="left:635px">Views</span><span style="left:676px">Last Message</span></div>
  <div class="threads">
    <div class="thread"><div class="avatar photo" role="img" aria-label="Member avatar"></div><div class="thread-main"><span class="tag article">Article</span>Wellcom to CALEDx, the new catalan MOOC directory<span class="meta">Jordi Malvet, Yesterday at 7:02 PM, Blog</span></div><div class="stats"><span>Replies:</span><span class="num">0</span><span class="sm">Views:</span><span class="sm num">28</span></div><div class="last">Jordi Malvet<span class="meta">Yesterday at 7:02 PM</span></div></div>
    <div class="thread"><div class="avatar">Vet<br>rola</div><div class="thread-main"><span class="tag courses">Courses</span>Norvane MOOCs<span class="meta">Marisa, Yesterday at 9:30 AM, openEdra</span></div><div class="stats"><span>Replies:</span><span class="num">0</span><span class="sm">Views:</span><span class="sm num">55</span></div><div class="last">Marisa<span class="meta">Yesterday at 9:30 AM</span></div></div>
    <div class="thread"><div class="avatar">Vet<br>rola</div><div class="thread-main"><span class="tag news">News</span>Vetrola's Course Scoop promoted to Gold level!<span class="meta">Marisa, Monday at 6:24 PM, MOOC News</span></div><div class="stats"><span>Replies:</span><span class="num">1</span><span class="sm">Views:</span><span class="sm num">47</span></div><div class="last">Teodor<span class="meta">Tuesday at 2:14 PM</span></div></div>
    <div class="thread"><div class="avatar">Vet<br>rola</div><div class="thread-main"><span class="tag news">News</span>Quill Academy are looking for a video star!<span class="meta">Marisa, Tuesday at 8:41 AM, General stuff on course providers</span></div><div class="stats"><span>Replies:</span><span class="num">0</span><span class="sm">Views:</span><span class="sm num">116</span></div><div class="last">Marisa<span class="meta">Tuesday at 8:41 AM</span></div></div>
    <div class="thread"><div class="avatar">Vet<br>rola</div><div class="thread-main"><span class="tag event">Event</span>What Reviews divulge about Online Education<span class="meta">Marisa, Monday at 10:52 AM, Events</span></div><div class="stats"><span>Replies:</span><span class="num">0</span><span class="sm">Views:</span><span class="sm num">76</span></div><div class="last">Marisa<span class="meta">Monday at 10:52 AM</span></div></div>
    <div class="thread tall"><div class="avatar blank"></div><div class="thread-main"><span class="tag advice">Advice</span>How do you "unenroll" from a course on Learnova?<span class="meta">Helen, Feb 13, 2015, MOOC Advice</span></div><div class="stats"><span>Replies:</span><span class="num">2</span><span class="sm">Views:</span><span class="sm num">3,482</span></div><div class="last">Ravi<span class="meta">Sunday at 11:01 PM</span></div></div>
    <div class="thread"><div class="avatar">Vet<br>rola</div><div class="thread-main"><span class="tag courses">Courses</span>6 top rated free courses starting in May<span class="meta">Marisa, May 13, 2015, Recommend a course here</span></div><div class="stats"><span>Replies:</span><span class="num">0</span><span class="sm">Views:</span><span class="sm num">152</span></div><div class="last">Marisa<span class="meta">May 13, 2015</span></div></div>
    <div class="thread"><div class="avatar">Vet<br>rola</div><div class="thread-main"><span class="tag news">News</span>The European MOOCs Scoreboard<span class="meta">Marisa, May 12, 2015, MOOC News</span></div><div class="stats"><span>Replies:</span><span class="num">0</span><span class="sm">Views:</span><span class="sm num">105</span></div><div class="last">Marisa<span class="meta">May 12, 2015</span></div></div>
  </div>
  <div class="pager">◀ ▶</div>
</section>

<footer class="footer">
  <div class="social"><i style="background:#3b5998"></i><i style="background:#1da1f2"></i><i style="background:#e52d27"></i><i style="background:#dd4b39"></i></div>
  <div class="newsletter">Subscribe for Monthly Newsletter</div>
  <a class="subscribe" href="#">Subscribe</a>
  <nav class="footnav">
    <a class="current" href="#">Home</a><a href="#">Forums</a><a href="#">Resources</a><a href="#">Members</a><a href="#">FAQ</a><a href="#">Blog</a><a href="#">Vetrola Español</a><a href="#">Course Scoop</a><a class="login" href="#">Login</a>
  </nav>
</footer>
</body>
</html>
```